Web Design Project

We are an IT System Integrator. We provide Norvik 500 ERP System, CRM etc. We also provide hardware, networking servicing. Please look at www.brinquot.com.sg. They provide the same service as us. We like to redesign our web site. I will attached the color that I prefer for reference.

Our website is www.ravdu.com.sg.  It has been created about 14 years ago.  We are trying to revamp it with a new look and information.   The new website must be informative, fast.    I have attached an attachment which show the color that I prefer(brownish golden).   

Our competitor (www.brinquot.com) is carrying the same trade as us.  They have all the informations In their website that we will like to have.  Therefore I recommend you to take a look at my competitor website and have a better   
understanding on the kind of information I would like to have for my new website.

This project is guarantee to the person with the best design.  We can have it guarantee.

Target Market(s)

Corporate and companies

Industry/Entity Type

Hardware

```html
<!DOCTYPE html>
<html lang="en">
<head>
<meta charset="utf-8">
<title>Ravdu Information System</title>
<link href="https://fonts.googleapis.com/css2?family=Source+Sans+3:ital,wght@0,400;0,600;0,700;1,400&display=swap" rel="stylesheet">
<style>
:root{
  --brown:#85622d;
  --gold:#b09158;
  --text-brown:#7d5c26;
  --ink:#2b2b2b;
  --panel-top:#f1f1f1;
  --panel-bottom:#d8d8d8;
  --panel-line:#bdbdbd;
  --white:#fff;
  --caption:#262a2e;
}
*{box-sizing:border-box;margin:0;padding:0}
html,body{width:1015px;height:1200px;overflow:hidden;background:var(--white)}
body{position:relative;font-family:"Source Sans 3",sans-serif;color:var(--ink)}
.abs{position:absolute}
.top-bar{left:0;top:0;width:1015px;height:12px;background:var(--brown)}
.nav-btn{height:32px;width:97px;background:var(--brown);color:var(--white);font-size:13.5px;display:flex;align-items:center;justify-content:center;top:49px;text-decoration:none}
.hero-band{left:0;top:107px;width:1015px;height:369px;background:var(--gold)}
.hero-photo{left:97px;top:121px;width:812px;height:341px;background:radial-gradient(ellipse at 35% 45%,#f3d9c6 0%,#e7c3ad 25%,#cfd4da 55%,#e9ecef 80%,#f5f5f5 100%)}
.caption{left:567px;top:354px;width:327px;height:90px;background:var(--caption);color:var(--white);padding:13px 22px}
.caption h2{font-size:16.5px;font-weight:700;margin-bottom:8px}
.caption p{font-size:12.5px;line-height:16px}
.shield{left:410px;top:12px;width:192px;height:133px}
.brand{left:410px;top:58px;width:192px;text-align:center;font-size:14px;font-weight:700;color:#4a3412;display:flex;align-items:center;justify-content:center;gap:6px}
.brand-dot{width:9px;height:9px;border-radius:50%;background:#4a3412}
.welcome{left:108px;top:500px;font-size:25px;font-weight:400;color:var(--text-brown)}
.welcome strong{font-weight:700}
.intro{left:108px;top:554px;width:530px;font-size:12.7px;line-height:16.2px}
.intro p{margin-bottom:16px}
.intro .accent{color:var(--text-brown);font-style:italic}
.read-more{color:var(--text-brown);font-size:13.5px}
.intro-more{left:552px;top:772px}
.news-panel{left:110px;top:816px;width:554px;height:291px;background:var(--gold)}
.news-panel h3{position:absolute;top:20px;font-size:19px;font-weight:400;color:var(--white)}
.card{position:absolute;top:63px;width:240px;height:201px;background:linear-gradient(var(--panel-top),var(--panel-bottom));padding:24px 16px}
.card p{font-size:13px;line-height:16.3px;margin-bottom:16px}
.card .event{font-weight:700;font-size:13px;margin-bottom:16px}
.card .read-more{position:absolute;right:18px;bottom:14px}
.side-box{left:711px;width:216px;border:1px solid var(--panel-line);border-radius:4px;background:linear-gradient(var(--panel-top),var(--panel-bottom))}
.side-box h4{font-size:14px;font-weight:700;color:var(--text-brown);letter-spacing:.4px}
.login{top:490px;height:155px;padding:14px 16px}
.field{display:block;width:130px;height:24px;border:1px solid #ccc;background:var(--white);font-size:10px;color:#999;padding:5px 11px;margin-top:8px;letter-spacing:.3px}
.field:first-of-type{margin-top:18px}
.login-actions{display:flex;align-items:center;gap:12px;margin-top:10px;font-size:10.5px;letter-spacing:.6px}
.login-btn{background:var(--gold);color:var(--white);padding:4px 8px}
.register{color:var(--gold)}
.badge-box{left:711px;top:656px;width:216px;height:146px;background:var(--gold);border-radius:4px}
.badge-shape{position:absolute;left:33px;top:22px;width:150px;height:42px;border-radius:21px;background:var(--white)}
.badge-bar{position:absolute;left:13px;top:94px;width:190px;height:40px;background:var(--white)}
.testimonials{top:816px;height:262px;padding:14px 18px}
.quote{font-size:10.8px;font-style:italic;line-height:14px;margin-top:14px}
.author{font-size:11px;font-style:italic;color:var(--text-brown);text-align:right;margin-top:6px;padding-right:10px}
.divider{height:1px;background:var(--gold);margin:14px 0 0}
.view-btn{display:inline-block;margin-top:20px;background:var(--gold);color:var(--white);font-size:9.5px;padding:5px 10px}
.footer{left:0;top:1151px;width:1015px;height:49px;background:var(--brown)}
</style>
</head>
<body>
<div class="abs top-bar"></div>

<nav>
  <a class="abs nav-btn" style="left:173px" href="#">HOME</a>
  <a class="abs nav-btn" style="left:283px" href="#">ABOUT</a>
  <a class="abs nav-btn" style="left:630px" href="#">SOLUTIONS</a>
  <a class="abs nav-btn" style="left:740px" href="#">SERVICES</a>
</nav>

<div class="abs hero-band"></div>
<div class="abs hero-photo" role="img" aria-label="Photo of a smiling support agent wearing a headset in a bright office"></div>
<div class="abs caption">
  <h2>Lorem ipsum dolor sit amet</h2>
  <p>Consectetur adipiscing elit. Sit und faq et meae dolor ipsum uanime sinquera consecteter elit.</p>
</div>

<svg class="abs shield" viewBox="0 0 192 133">
  <defs>
    <linearGradient id="shieldFill" x1="0" y1="0" x2="1" y2="1">
      <stop offset="0" stop-color="#8c6a35"/>
      <stop offset=".5" stop-color="#d9c79d"/>
      <stop offset="1" stop-color="#a78a55"/>
    </linearGradient>
  </defs>
  <polygon points="0,0 192,0 192,111 96,133 0,111" fill="var(--brown)"/>
  <polygon points="6,0 186,0 186,106 96,126 6,106" fill="url(#shieldFill)"/>
</svg>
<div class="abs brand"><span class="brand-dot"></span>Ravdu Information System</div>

<h1 class="abs welcome">Welcome To <strong>Ravdu Information System</strong></h1>
<div class="abs intro">
  <p>Lorem ipsum dolor sit amet consectetur adipiscing elit, sit und faq enea meum sit comepare und faq consectetur elit amet ipsum lorem et sinae flammis et undeanara sind quid. Lorem ipsum dolor sit amet consectetur adipiscing elit, sit und faq enea meum sit comepare und faq consectetur elit amet ipsum lorem et sinae flammis et undeanara sind quid. Lorem ipsum dolor sit amet consectetur adipiscing elit, sit und faq enea meum sit comepare und faq consectetur elit amet ipsum lorem et sinae flammis et undeanara sind quid.</p>
  <p class="accent">Lorem ipsum dolor sit amet consectetur adipiscing elit, sit und faq enea meum sit comepare und faq consectetur elit amet ipsum lorem et sinae flammis et undeanara sind quid.</p>
  <p>Lorem ipsum dolor sit amet consectetur adipiscing elit, sit und faq enea meum sit comepare und faq consectetur elit amet ipsum lorem et sinae flammis et undeanara sind quid. Lorem ipsum dolor sit amet consectetur adipiscing consectetur elit amet.</p>
</div>
<span class="abs read-more intro-more">READ MORE</span>

<section class="abs news-panel">
  <h3 style="left:25px">Latest News</h3>
  <h3 style="left:289px">Future Events</h3>
  <div class="card" style="left:25px">
    <p>Lorem ipsum dolor sit amet consectetur adipiscing elit, et und faq inae elit consectetur dolor ipsum lorem manus et sisticus et faq.</p>
    <p>Lorem ipsum dolor sit amet faq inae elit consectetur dolor ipsum lorem manus et sisticus et faq.</p>
    <span class="read-more">READ MORE</span>
  </div>
  <div class="card" style="left:289px">
    <div class="event">Lorem Ipsum Dolor 2013</div>
    <div class="event">Consectetur Sit Amet 4</div>
    <div class="event">Adipiscing Elit Sit amet 2013</div>
    <div class="event">Ipsum Consectetur 2013</div>
    <span class="read-more">VIEW MORE</span>
  </div>
</section>

<aside>
  <div class="abs side-box login">
    <h4>USER LOGIN</h4>
    <span class="field">username</span>
    <span class="field">password</span>
    <div class="login-actions"><span class="login-btn">LOGIN</span><span class="register">REGISTER</span></div>
  </div>
  <div class="abs badge-box" role="img" aria-label="Partner certification badge">
    <div class="badge-shape"></div>
    <div class="badge-bar"></div>
  </div>
  <div class="abs side-box testimonials">
    <h4>Testimonials</h4>
    <p class="quote">Lorem ipsum dolor sit amet, consectetur adipiscing elit et und faq elit dolor consectetur ipsum dolor.</p>
    <p class="author">Delia Marwood</p>
    <div class="divider"></div>
    <p class="quote">Lorem ipsum dolor sit amet, consectetur adipiscing elit et und faq elit dolor consectetur ipsum dolor.</p>
    <p class="author">Owen Trelawny</p>
    <span class="view-btn">VIEW MORE</span>
  </div>
</aside>

<footer class="abs footer"></footer>
</body>
</html>
```